Brazilian-Italian food blogger looks for a yummy design for her blog

Ciao everyone! I am looking for a brand new design for my Wordpress food blog, MaRuPAN (marupan.net). The blog is about my deep love with food and with Bologna. I write particularly for the Brazilian crowd.
I talk about gastronomic curiosities of the town, delicious places and specialties that one can only find here. There are also many posts about my trips around Italy.
I would like the new design to be more sophisticated (or should I say professional?), but friendly at the same time.
If possible, I would like to keep its background very clean (if there are patters related to food, like the way it is now, even better), especially because I post many big colourful photos...
Also, since it is a personal blog, I would love if visitors could see a picture of mine and with a short description right at the homepage.
Thank you so much in advance.
Cheers,
Telma.

Target Market(s)

Brazilian people interested in Italian culture and gastronomy.

Colors
fcca95

Requirements
Must have
• A neutral background that does not interfere with photos.
• My photo with a short description on the homepage.
Nice to have
• A background that has something to do with food.
Should not have
• It should not look like a girly blog.

```html
<!DOCTYPE html>
<html lang="pt">
<head>
<meta charset="utf-8">
<title>MaRuPAN – Minha declaração de amor ao comer bem e a Bologna</title>
<link href="https://fonts.googleapis.com/css2?family=Fjord+One&family=Arimo:wght@400;700&display=swap" rel="stylesheet">
<style>
:root{
  --tan:#c09e6e;
  --cream:#fcecbd;
  --band:#e3a06a;
  --band-dark:#a86a3c;
  --ink:#3a2414;
  --text:#6b5a44;
  --link:#d9783a;
  --pattern:#ededed;
  --footer:#3b2a22;
  --white:#ffffff;
}
*{box-sizing:border-box;margin:0;padding:0}
html,body{width:1200px;height:2759px;overflow:hidden}
body{position:relative;background:var(--pattern);font-family:"Arimo",Arial,sans-serif;color:var(--text);font-size:11.5px;line-height:1.45}
.abs{position:absolute}
.food-pattern{left:0;top:552px;width:1200px;height:2207px;background:var(--pattern)}
.header-band{left:0;top:0;width:1200px;height:552px;background:var(--tan)}
.site-name{left:108px;top:14px;display:flex;align-items:center;gap:10px;font-family:"Fjord One",serif;font-size:30px;color:var(--ink);line-height:1;text-transform:uppercase;letter-spacing:2px}
.site-name i{display:block;width:14px;height:14px;background:var(--ink)}
.search{left:823px;top:24px;display:flex}
.search span{display:block;width:180px;height:24px;background:var(--white);font-size:11px;color:#aaa;padding:4px 6px}
.search b{display:block;width:66px;height:24px;background:#3a2418;color:var(--white);font-size:10px;text-align:center;line-height:24px}
.slider{left:108px;top:76px;width:961px;height:400px;background:var(--cream);padding:22px 0 4px 23px}
.slider-photo{width:938px;height:374px;background:linear-gradient(180deg,#5878c8 0%,#a8b8e0 35%,#a85a3c 55%,#7a3e2a 100%)}
.slider-arrow{top:242px;width:58px;height:96px;border-radius:50%;background:var(--cream);display:flex;align-items:center;justify-content:center}
.slider-arrow.prev{left:70px}.slider-arrow.next{left:1070px;width:62px}
.nav{left:108px;top:476px;width:961px;height:57px;background:var(--band);display:flex;align-items:center;padding-left:42px;gap:38px;font-family:"Fjord One",serif;font-weight:bold;font-size:19px;color:var(--ink)}
.content{left:108px;top:552px;width:961px;height:2122px;background:var(--cream)}
.post-title{left:108px;width:690px;height:48px;background:var(--band);color:var(--white);font-family:"Fjord One",serif;font-size:21px;padding:9px 30px}
.fold{width:0;height:0;border-top:12px solid var(--band-dark);border-left:14px solid transparent}
.meta{left:140px;font-size:11.5px;color:var(--ink)}
.meta a,.link{color:var(--link);text-decoration:underline}
.photo{border-radius:2px}
.excerpt{font-size:11.5px;color:var(--text)}
.excerpt p{margin-bottom:12px}
.excerpt.loose{line-height:1.75}
.read-more{left:697px;width:100px;height:23px;background:var(--band);color:var(--white);font-size:12px;text-align:center;line-height:23px}
.rule{left:140px;width:658px;height:1px;background:#e5cf95}
.quote{left:150px;width:160px;font-style:italic;color:#a99a82;font-size:11.5px}
.quote-mark{font-family:"Fjord One",serif;font-size:34px;color:#cbbfa8;line-height:1}
.pager{left:416px;top:2593px;display:flex;gap:8px;font-size:12px}
.pager span{display:block;padding:2px 7px}
.pager .current{background:#c4382b;color:var(--white)}
.footer{left:108px;top:2674px;width:961px;height:73px;background:var(--footer);color:#d8c8b0;font-size:11px;padding:28px 30px}
.footer a{color:var(--link)}
.side-title{left:823px;width:267px;height:40px;background:var(--band);color:var(--white);font-family:"Fjord One",serif;font-size:19px;padding:7px 32px}
.side-fold{left:1076px;border-top:12px solid var(--band-dark);border-right:14px solid transparent;border-left:0}
.about-photo{left:908px;top:644px;width:96px;height:96px;background:linear-gradient(160deg,#3a2c2a,#8a6e5e)}
.about-text{left:823px;top:755px;width:267px;text-align:center;font-size:10.5px;color:var(--ink)}
.like-box{left:823px;top:885px;width:255px;font-size:10px;color:var(--ink)}
.like-mark{width:48px;height:46px;background:#6b5a8a}
.like-btn{display:inline-block;background:#4a64a0;color:var(--white);font-size:9px;padding:1px 5px;margin-top:3px}
.fans{display:grid;grid-template-columns:repeat(6,38px);gap:4px;margin-top:14px}
.fans div{height:38px}
.recent{left:830px;width:255px;font-size:10px;color:var(--text);display:grid;grid-template-columns:50px 50px 1fr;column-gap:6px;line-height:1.3}
.recent .day{font-family:"Fjord One",serif;font-size:22px;color:var(--ink);text-align:center;line-height:1}
.recent .month{font-size:9px;color:var(--ink);text-align:center}
.recent .thumb{width:50px;height:38px}
.recent .more{grid-column:1/4;margin-top:2px}
.cats{left:842px;top:1936px;font-size:11px;list-style:none}
.cats li{margin-bottom:18px}
.cats li::before{content:"• ";color:var(--ink)}
</style>
</head>
<body>
<div class="abs food-pattern" role="img" aria-label="Fundo claro com padrão de talheres cinza"></div>
<header>
  <div class="abs header-band"></div>
  <div class="abs site-name"><i></i>MaRuPAN</div>
  <div class="abs search"><span>Search</span><b>SEARCH</b></div>
  <div class="abs slider-arrow prev"><svg width="20" height="36" viewBox="0 0 20 36"><path d="M16 2 L3 18 L16 34" fill="none" stroke="#d9c79a" stroke-width="2"/></svg></div>
  <div class="abs slider-arrow next"><svg width="20" height="36" viewBox="0 0 20 36"><path d="M4 2 L17 18 L4 34" fill="none" stroke="#d9c79a" stroke-width="2"/></svg></div>
  <div class="abs slider"><div class="slider-photo" role="img" aria-label="Telhados e torres medievais de Bologna sob céu azul"></div></div>
  <nav class="abs nav"><span>Home</span><span>O blog</span><span>Bella Bo</span><span>BUONI POSTI</span><span>Eu, Telma</span><span>FUORI CASA</span><span>Contato</span></nav>
</header>

<div class="abs content"></div>

<main>
  <h2 class="abs post-title" style="top:593px">Dando de barato</h2>
  <div class="abs fold" style="left:108px;top:641px"></div>
  <p class="abs meta" style="top:668px">Posted in <a>Pasta</a> on September 16, 2014 <a>No comments</a></p>
  <div class="abs photo" style="left:140px;top:697px;width:154px;height:96px;background:radial-gradient(circle,#f2d35a,#d9a838 60%,#f4efe2 62%)" role="img" aria-label="Prato de massa recheada"></div>
  <div class="abs excerpt" style="left:320px;top:695px;width:478px">
    <p>É inquietante como damos de barato certas coisas que, no fundo são excepcionais – e raras. A companhia de pessoas queridas, o litoral brasileiro, água-de-coco... Pequenas coisas que, ainda que muito especiais, por se tornarem corriqueiras nas nossas vidas, não damos o devido valor.</p>
    <p>Me dei conta que um desses exemplos é um dos restaurantes de que mais gosto aqui em Bologna, o <i>Sale Fino</i>.</p>
    <p>Bato ponto pelo menos uma vez por semana – já virou quase rotina – e por me sentir sempre em casa, por conhecer os chefs e os garçons, e, principalmente, porque comer bem ali é uma constância, deixei de perceber que a qualidade dos pratos do local é extraordinária, e muito difícil de se replicada.</p>
  </div>
  <p class="abs excerpt" style="left:140px;top:902px">O Sale Fino é um dos raros exemplos de cozinha meridional (i.e. ...</p>
  <div class="abs read-more" style="top:947px">read more</div>
  <div class="abs rule" style="top:988px"></div>

  <h2 class="abs post-title" style="top:1035px">Mortadella Bologna</h2>
  <div class="abs fold" style="left:108px;top:1083px"></div>
  <p class="abs meta" style="top:1110px">Posted in <a>Uncategorized</a> on September 16, 2014 <a>No comments</a></p>
  <div class="abs photo" style="left:140px;top:1133px;width:170px;height:154px;background:linear-gradient(160deg,#c7b46a,#8a6a3a 60%,#d8b888)" role="img" aria-label="Mortadelas penduradas numa vitrine"></div>
  <p class="abs excerpt" style="left:322px;top:1133px;width:476px">Em uma pequena ruazinha chamada Vicolo Granelli, bem no centro histórico de Bologna, há uma placa, redonda, com os seguintes dizeres:</p>
  <div class="abs photo" style="left:402px;top:1179px;width:281px;height:281px;background:radial-gradient(circle,#efe6d4 45%,#b9ad98 55%,#8a7c66)" role="img" aria-label="Placa redonda de pedra com inscrição sobre a mortadela"></div>
  <div class="abs quote" style="top:1295px"><div class="quote-mark">“</div>"Esta casa era a sede, de 1242 a 1796, da arte dos Salaroli, que controlavam a produção dos salumi Bolognesi, dos quais a excelente mortadela foi grande no mundo o mito de Bologna "la grassa" ("a gorda")".<div class="quote-mark" style="text-align:right">”</div></div>
  <p class="abs excerpt" style="left:322px;top:1474px;width:476px">Em outras palavras, foi bem ali que a história do embutido cor-de-rosa mais querido do mundo se misturou à de Bologna, a ponto de receber o próprio nome da cidade, "<i>Mortadella Bologna</i>".</p>
  <div class="abs excerpt" style="left:140px;top:1536px;width:658px">
    <p>Os Salaroli (ou Salaroli), mencionados na placa, eram os membros da cooperativa mais antiga de produtores de fios da região, responsáveis pela elaboração de mortadela e outros salumi desde o século XII.</p>
    <p>Sua história é peculiar: antes de se...</p>
  </div>
  <div class="abs read-more" style="top:1627px">read more</div>
  <div class="abs rule" style="top:1662px"></div>

  <h2 class="abs post-title" style="top:1672px">Simplesmente pão e leite</h2>
  <div class="abs fold" style="left:108px;top:1720px"></div>
  <p class="abs meta" style="top:1730px">Posted in <a>Sweets</a> on September 16, 2014 <a>No comments</a></p>
  <div class="abs photo" style="left:140px;top:1752px;width:113px;height:147px;background:linear-gradient(170deg,#6e5a3a,#d8b86a 50%,#8a7a52)" role="img" aria-label="Pão doce e leite numa mesa"></div>
  <div class="abs excerpt loose" style="left:270px;top:1752px;width:528px">
    <p>No fim de semana passado, escapei (de novo) para a montanha, desta vez para as Dolomitas, no Trentino-Alto Adige. Essa é uma região muito particular da Itália, onde a primeira língua é o alemão, e, de tão organizada e precisa, qualquer italiano vindo de outro lugar se sente um peixe fora d'água.</p>
    <p>Mas, de jeito nenhum digo isso em modo depreciativo: é uma delícia rodar por estradas sem buracos, visitar lugares turísticos (como as trilhas da Marmolada, uma montanha perenemente coberta de neve, ou aquelas que levam ao alto dos 3.152m do Piz Boè) sem se perder no meio do caminho. Sem falar que é muito divertido ouvir as pessoas misturarem o alemão com o italiano sem perceber.</p>
  </div>
  <div class="abs excerpt" style="left:140px;top:1995px;width:658px">
    <p>Porém, confesso ficaram duas coisas muito simples que mais me impressionaram: o pão e o iogurte.</p>
    <p>Isso mesmo.</p>
  </div>
  <div class="abs read-more" style="top:2070px">read more</div>
  <div class="abs rule" style="top:2112px"></div>

  <h2 class="abs post-title" style="top:2154px">Insalata di riso della Giuliana</h2>
  <div class="abs fold" style="left:108px;top:2202px"></div>
  <p class="abs meta" style="top:2229px">Posted in <a>Riso</a> on September 16, 2014 <a>No comments</a></p>
  <div class="abs photo" style="left:140px;top:2253px;width:143px;height:161px;background:radial-gradient(circle,#f2e6b8,#d8b046 45%,#7a9a3a 80%)" role="img" aria-label="Salada de arroz colorida com legumes"></div>
  <div class="abs excerpt" style="left:300px;top:2253px;width:498px">
    <p>Dizem aqui que toda menina italiana tem sua receita de <i>insalata di riso</i>. Sinceramente não sei quanto seja verdade e, confesso, receita mesmo eu só tenho a do <i>farro</i> (já mostrei aqui). Mas, para me garantir, peguei emprestada a receita da minha sogra e, como funciona tão bem, não pretendo mudar.</p>
    <p>A <i>insalata di riso</i> é muito comum nas mesas italianas, de norte a sul. Mesmo nas lojas que vendem comidas prontas, ela marca presença quase o ano todo.</p>
  </div>
  <p class="abs excerpt" style="left:140px;top:2428px;width:658px">Mas o bacana mesmo é que não existe uma receita típica; em cada esquina ela tem uma cara diferente. A única coisa em comum é o fato de ser feita com arroz e essencialmente coisinhas que qualquer um compra já prontas no supermercado: atum, azeitona, ervilhas, queijo, conservas, presunto, salsicha, e por aí vai...</p>
  <div class="abs read-more" style="top:2484px">read more</div>
  <div class="abs rule" style="top:2530px"></div>

  <div class="abs pager"><span class="current">1</span><span class="link">2</span><span class="link">Next »</span></div>
</main>

<aside>
  <h3 class="abs side-title" style="top:586px">About</h3>
  <div class="abs fold side-fold" style="top:626px"></div>
  <div class="abs about-photo" role="img" aria-label="Retrato da autora do blog"></div>
  <div class="abs about-text">MaRuPAN<br>Minha declaração de amor ao comer bem e a Bologna</div>

  <h3 class="abs side-title" style="top:828px">Like the blog</h3>
  <div class="abs fold side-fold" style="top:868px"></div>
  <div class="abs like-box">
    <div style="display:flex;gap:6px;margin-left:10px">
      <div class="like-mark"></div>
      <div><b>MaRuPAN</b><br><span class="like-btn">■ Like</span></div>
    </div>
    <p style="margin:8px 0 0 10px">144 people like MaRuPAN.</p>
    <div class="fans" style="margin-left:10px">
      <div style="background:#7a6a5a"></div><div style="background:#a89888"></div><div style="background:#5a4a3a"></div><div style="background:#8a8478"></div><div style="background:#b8a894"></div><div style="background:#6a5a52"></div>
      <div style="background:#9a8a7a"></div><div style="background:#5a6a7a"></div><div style="background:#8a7a6a"></div><div style="background:#c8b8a4"></div><div style="background:#6a7a8a"></div><div style="background:#7a6a62"></div>
    </div>
    <p style="margin:18px 0 0 10px;font-size:9px">■ Social plugin</p>
  </div>

  <h3 class="abs side-title" style="top:1133px">Recent Posts</h3>
  <div class="abs fold side-fold" style="top:1173px"></div>
  <div class="abs recent" style="top:1214px"><div><div class="day">16</div><div class="month">September</div></div><div class="thumb" style="background:#e0b848"></div><div><a class="link">Dando de barato</a><br>É inquietante como damos de barato certas</div><div class="more">coisas que, no fundo são excepcionais – e raras...</div></div>
  <div class="abs recent" style="top:1326px"><div><div class="day">16</div><div class="month">September</div></div><div class="thumb" style="background:#a89a5a"></div><div><a class="link">Mortadella Bologna</a><br>Em uma pequena ruazinha chamada</div><div class="more">Vicolo Granelli, bem no centro histórico de Bologna, há uma placa, redonda, com os segui...</div></div>
  <div class="abs recent" style="top:1436px"><div><div class="day">16</div><div class="month">September</div></div><div class="thumb" style="background:#9a845a"></div><div><a class="link">Simplesmente pão e leite</a><br>No fim de semana passado, escapei</div><div class="more">(de novo) para a montanha, desta vez para as Dolomitas, no Trentino-Alto Adige...</div></div>
  <div class="abs recent" style="top:1546px"><div><div class="day">16</div><div class="month">September</div></div><div class="thumb" style="background:#c8a840"></div><div><a class="link">Insalata di riso della Giuliana</a><br>Dizem aqui que toda menina</div><div class="more">italiana tem sua receita de insalata di riso...</div></div>
  <div class="abs recent" style="top:1644px"><div><div class="day">14</div><div class="month">September</div></div><div class="thumb" style="background:#b87a4a"></div><div><a class="link">Tradução</a><br>Em uma visita zás-trás por São Paulo, me dei conta que,</div><div class="more">além de todo o mais, sinto realmente falta de algumas comidas "d...</div></div>
  <div class="abs recent" style="top:1752px"><div><div class="day">13</div><div class="month">September</div></div><div class="thumb" style="background:#e8c838"></div><div><a class="link">Montanha mágica</a><br>Não sei se é mal de brasileiro, ou</div><div class="more">se é meu mesmo, mas quando o calor de verdade (tipo mais de 32 graus) começa a pegar, q...</div></div>

  <h3 class="abs side-title" style="top:1870px">Categories</h3>
  <div class="abs fold side-fold" style="top:1910px"></div>
  <ul class="abs cats">
    <li><a class="link">Bologna</a></li>
    <li><a class="link">Pasta</a></li>
    <li><a class="link">Riso</a></li>
    <li><a class="link">Sweets</a></li>
    <li><a class="link">Uncategorized</a></li>
  </ul>
</aside>

<footer class="abs footer">Copyright © 2014 <a>MaRuPAN</a></footer>
</body>
</html>
```